New business card for UK roofing company

We are Brindmore Roofing and we need a business card design for our staff.

We offer the following services:

- New roofs
- General roof repairs
- Drone surveys
- Single ply roofing
- Steel cladding
- Asbestos removal
- Electronic leak detection

I have attached our logo. I have also attached example branding printed to our vans. The business card should fit in with the style of our branding.

The business card should have the following information;

Address:
Unit 17c Wendlecroft Farm
Wendlecroft Lane
Hatchington
CM4 9QD

Telephone: 020 7946 0372
24 Hour: 0800 612 4479

Email: ray@brindmoreroofing.example
Mobile: 07700981234
Name: Ray Tunstead
Website: www.brindmoreroofing.example

The business card will be printed in Spot UV, see here: https://www.kestaprint.example/business-cards/spot-uv/

If you need anymore info, please let me know,

```html
<!DOCTYPE html>
<html lang="en">
<head>
<meta charset="utf-8">
<title>Brindmore Roofing – Business Card</title>
<link href="https://fonts.googleapis.com/css2?family=Montserrat:wght@400;500;700&display=swap" rel="stylesheet">
<style>
  :root {
    --navy: #0f4a7e;
    --navy-deep: #0b3d6b;
    --sky: #12aee0;
    --paper: #ffffff;
    --stage: #e9ecef;
    --ink-light: #d8e8f5;
  }
  * { box-sizing: border-box; margin: 0; padding: 0; }
  html, body { width: 1200px; height: 801px; overflow: hidden; }
  body {
    background: var(--stage);
    font-family: "Montserrat", Arial, sans-serif;
    display: flex; align-items: center; justify-content: center; gap: 40px;
  }
  .card {
    width: 540px; height: 340px; position: relative; overflow: hidden;
    box-shadow: 0 8px 24px rgba(0,0,0,.18);
  }
  /* Front */
  .card--front { background: var(--paper); }
  .contact-band {
    position: absolute; left: 0; top: 0; width: 362px; height: 188px;
    background: var(--navy);
    border-bottom: 4px solid var(--sky);
  }
  .staff-name {
    position: absolute; left: 22px; top: 26px;
    color: var(--sky); font-weight: 700; font-size: 21px; letter-spacing: .5px;
    white-space: nowrap;
  }
  .contact-list { position: absolute; left: 22px; top: 66px; list-style: none; }
  .contact-list li {
    display: flex; align-items: center; gap: 7px;
    color: var(--paper); font-size: 12px; line-height: 21px; white-space: nowrap;
  }
  .contact-list svg { width: 10px; height: 10px; fill: var(--ink-light); flex: none; }
  .band-divider {
    position: absolute; left: 208px; top: 22px; width: 1px; height: 78px;
    background: var(--sky);
  }
  .address {
    position: absolute; left: 218px; top: 26px; font-style: normal;
    color: var(--paper); font-size: 10px; line-height: 16px; white-space: nowrap;
  }
  .services { position: absolute; left: 22px; top: 210px; }
  .services-title { color: var(--navy); font-weight: 700; font-size: 15px; margin-bottom: 8px; }
  .services-cols { display: flex; gap: 26px; }
  .services-cols ul { list-style: none; }
  .services-cols li {
    color: var(--navy-deep); font-size: 12px; line-height: 20px; position: relative; padding-left: 11px;
  }
  .services-cols li::before {
    content: ""; position: absolute; left: 0; top: 8px; width: 5px; height: 5px;
    border-radius: 50%; background: var(--sky);
  }
  .brand-mark {
    position: absolute; right: 8px; top: 40px; width: 164px;
    display: flex; flex-direction: column; align-items: center; gap: 12px;
  }
  .brand-mark__dot { width: 120px; height: 120px; border-radius: 50%; background: var(--sky); }
  .brand-mark__name { color: var(--navy); font-weight: 700; font-size: 15px; white-space: nowrap; }
  /* Back */
  .card--back {
    background: linear-gradient(115deg, var(--navy-deep) 0%, var(--navy) 45%, var(--sky) 100%);
    display: flex; align-items: center; justify-content: center; gap: 16px;
  }
  .back-mark__dot { width: 54px; height: 54px; border-radius: 50%; background: var(--sky); }
  .back-mark__name { color: var(--paper); font-weight: 700; font-size: 34px; letter-spacing: -.5px; }
</style>
</head>
<body>
  <section class="card card--front">
    <div class="contact-band">
      <h1 class="staff-name">RAY TUNSTEAD</h1>
      <div class="band-divider"></div>
      <address class="address">
        Unit 17c Wendlecroft Farm<br>Wendlecroft Lane<br>Hatchington CM4 9QD
      </address>
      <ul class="contact-list">
        <li><svg viewBox="0 0 10 10"><rect x="2.5" y="0" width="5" height="10" rx="1"/></svg>07700981234</li>
        <li><svg viewBox="0 0 10 10"><path d="M2 0l2 2-1 2 3 3 2-1 2 2-2 2C4 10 0 6 0 2z"/></svg>020 7946 0372</li>
        <li><svg viewBox="0 0 10 10"><circle cx="5" cy="5" r="5"/></svg>0800 612 4479</li>
        <li><svg viewBox="0 0 10 10"><path d="M0 2h10v6H0z"/></svg>ray@brindmoreroofing.example</li>
        <li><svg viewBox="0 0 10 10"><circle cx="5" cy="5" r="5"/></svg>www.brindmoreroofing.example</li>
      </ul>
    </div>

    <div class="services">
      <h2 class="services-title">We offer the following services:</h2>
      <div class="services-cols">
        <ul>
          <li>New roofs</li>
          <li>General roof repairs</li>
          <li>Drone surveys</li>
          <li>Electronic leak detection</li>
        </ul>
        <ul>
          <li>Single ply roofing</li>
          <li>Steel cladding</li>
          <li>Asbestos removal</li>
        </ul>
      </div>
    </div>

    <div class="brand-mark">
      <div class="brand-mark__dot"></div>
      <span class="brand-mark__name">Brindmore Roofing</span>
    </div>
  </section>

  <section class="card card--back">
    <div class="back-mark__dot"></div>
    <span class="back-mark__name">Brindmore Roofing</span>
  </section>
</body>
</html>
```